Book Cover Design (poetry, prose, and original quotes Book) - Title: resonance & reflection

FIRSTLY - my name is MARGOT VELDHUIS (pls use this)

Looking for a soft cover design (6" X 9") as well as an e-book cover design. I have ISBN bar code already. This soft cover will need spine design and area for back cover blurb. Number of pages is approx 210. The page count might change, but only by a few pages if anything.
The book is a collection of poems, prose, and quotes with chapter titles such as: pain, growth, hope, trust, love, and...so it is. It's meant to be inspiring and also a go to book people will reach for when searching for truth.

Tavi Mendel and Odo Marrek are similar in nature to content.

I have attached an PIXORAMA image that I am thinking of.
Lower case in title and in my name (author)
San Serif font.

I like the idea of the book title to be along the lateral line (where water meets the sky).

I am open to book cover ideas like the poets noted above, but that style seems to be saturating the genre.

Target Market(s)

Will be selling on QBL (Borvex). Audience are people who are on a journey of self-discovery, personal empowerment, and spirituality.

Industry/Entity Type

Spiritual / Personal Growth / Poetry

Font styles to use
Sans Serif
Other font styles liked:
• Simplifica, alcubierre, stellar, gantic, kiona

Requirements
Must have
• Front, Spine, and Back cover / lower case in title and author's name
Nice to have
• I do like the look of Tavi Mendel and Odo Marrek's books, but I feel that style might be over done now, but I am open to a modern simple style like their books (see examples below). I would like my book to convey the feeling of resonance (vibration) and reflection (thoughts, ideas as a result of meditation)
Should not have
• I prefer simple designs, not a lot of clutter, or heavy typefaces. Definately do not want anything like birds or butterflies.

```html
<!DOCTYPE html>
<html lang="en">
<head>
<meta charset="utf-8">
<title>resonance &amp; reflection — cover spread</title>
<link rel="stylesheet" href="https://fonts.googleapis.com/css2?family=Oswald:wght@200;300&family=Montserrat:wght@300;400&display=swap">
<style>
  :root {
    --page: #fdfdfd;
    --back-blue: #bcd8e2;
    --title-teal: #3c6d81;
    --ink: #3a3d40;
    --spine-light: #f1f4f6;
    --sky-top: #d5dde3;
    --sky-low: #dfe4e9;
    --ridge: #3f6477;
    --forest: #121517;
    --water-dark: #1c2f3a;
    --water-mid: #3a6479;
    --water-light: #bccad3;
  }
  html, body {
    margin: 0;
    width: 1200px;
    height: 1200px;
    overflow: hidden;
    background: var(--page);
  }
  .canvas {
    position: relative;
    width: 1200px;
    height: 1200px;
  }
  .spread {
    position: absolute;
    left: 39px;
    top: 35px;
    width: 1122px;
    height: 807px;
  }
  .back-cover {
    position: absolute;
    left: 0;
    top: 0;
    width: 538px;
    height: 807px;
    background: var(--back-blue);
  }
  .front-photo {
    position: absolute;
    left: 538px;
    top: 0;
    width: 584px;
    height: 807px;
    background: linear-gradient(180deg,
      var(--sky-top) 0%,
      var(--sky-low) 38%,
      #b9ccd7 44%,
      var(--ridge) 52%,
      var(--forest) 62%,
      var(--water-dark) 68%,
      var(--water-mid) 76%,
      var(--water-light) 86%,
      #6f95a8 100%);
  }
  .title {
    position: absolute;
    margin: 0;
    font-family: "Oswald", sans-serif;
    font-weight: 200;
    color: var(--title-teal);
    font-size: 86px;
    line-height: 86px;
    text-align: right;
    letter-spacing: -0.5px;
  }
  .title .line { display: block; }
  .title .amp {
    font-family: "Montserrat", sans-serif;
    font-weight: 300;
    color: var(--ink);
    font-size: 48px;
    margin-right: 10px;
  }
  .back-cover .title { right: 78px; top: 90px; }
  .front-title { right: 70px; top: 90px; }
  .blurb {
    position: absolute;
    left: 81px;
    top: 340px;
    width: 369px;
    margin: 0;
    font-family: "Montserrat", sans-serif;
    font-weight: 400;
    font-size: 13px;
    line-height: 23.5px;
    color: var(--ink);
    text-align: justify;
    text-align-last: center;
  }
  .isbn-area {
    position: absolute;
    left: 298px;
    top: 669px;
    width: 151px;
    height: 93px;
    background: #ffffff;
  }
  .front-author {
    position: absolute;
    right: 74px;
    top: 292px;
    margin: 0;
    font-family: "Montserrat", sans-serif;
    font-weight: 400;
    font-size: 18px;
    letter-spacing: 3px;
    color: var(--ink);
  }
  .spine-author, .spine-title {
    position: absolute;
    left: 558px;
    margin: 0;
    writing-mode: vertical-rl;
    white-space: nowrap;
  }
  .spine-author {
    top: 110px;
    font-family: "Montserrat", sans-serif;
    font-size: 11px;
    letter-spacing: 2px;
    color: var(--ink);
  }
  .spine-title {
    top: 475px;
    font-family: "Oswald", sans-serif;
    font-weight: 300;
    font-size: 11px;
    letter-spacing: 4.2px;
    color: var(--spine-light);
  }
</style>
</head>
<body>
<main class="canvas">
  <section class="spread">
    <div class="back-cover">
      <h2 class="title">
        <span class="line">resonance</span>
        <span class="line"><span class="amp">&amp;</span>reflection</span>
      </h2>
      <p class="blurb">Lorem Ipsum is simply dummy text of the printing and typesetting industry. Lorem Ipsum has been the industry's standard dummy text ever since the 1500s, when an unknown printer took a galley of type and scrambled it to make a type specimen book. It has survived not only five centuries, but also the leap into electronic typesetting, remaining essentially unchanged. It was popularised in the 1960s with the release of Korvane sheets containing Lorem Ipsum passages, and more recently with desktop publishing software like Pellum LayoutDesk including versions of Lorem Ipsum.</p>
      <div class="isbn-area"></div>
    </div>

    <div class="front-photo" role="img" aria-label="Photograph of a misty mountain lake with dark forested slopes mirrored in still water under a pale sky"></div>

    <p class="spine-author">MARGOT VELDHUIS</p>
    <p class="spine-title">RESONANCE &amp; REFLECTION</p>

    <h1 class="title front-title">
      <span class="line">resonance</span>
      <span class="line"><span class="amp">&amp;</span>reflection</span>
    </h1>
    <p class="front-author">MARGOT VELDHUIS</p>
  </section>
</main>
</body>
</html>
```